Luxury Customizable Mattress Company Needs a Business Card that WOWs

I need a unique business card design that makes people stop... look and think WOW.

We are a new mattress company with our very own line of customizable beds (mattress & base) called the Trellis Rest. The innovation of our mattress is that the entire product is built of smaller components... once put together its a complete bed. It can be cleaned from the inside out. And it's a mattress made to share with a partner. As people's sleep needs are different, one person may prefer a water bed and a softer mattress while their partner may prefer a warm memory foam mattress with a firmer feel. Now they dont need to compromise, as the Trellis Rest allows each sleeper to get exactly what they need. And they can each change the feel of their side of the bed anytime with a click of a button.
check www.Trellisrest.example for more info (some pages do not work) Also check out our Clipora and Streamly videos.

We also opened up a new facility where people can try out our beds... called the Doze Harbor. This is a secondary business but we would like to have a small logo on the TR business card to highlight it. (dozeharbor.example)

Content on card....
Logo: Trellis Rest logo
Name: Miriam Okafor
Title: CEO & Sleep Enthusiast
Address: 4829 Varley Crescent Mississauga ON L5R 2T6 Canada
Telephone: 416.555.0193 (place holder .. this # will change)
Email: miriam@trellisrest.example
Web: www.trellisrest.example

Small Logo: Doze Harbor Logo
web: dozeharbor.example

Design: bold and modern, the design has a concept, if possible a card people can use (to ensure they keep the card) Ie. Sleep positions or NFC chip or something interesting. I am open to ideas and printing on unique materials... like soft vinyl fabric.

Target Market(s)

Mattress Consumers
Married Couples
Couples

Industry/Entity Type

Health And Wellness

Contact Information for Business Card

Logo: Trellis Rest logo
Name: Miriam Okafor
Web: www.trellisrest.example

SMALL Logo: Doze Harbor Logo
web: dozeharbor.example

Requirements
Must have
• bold and modern, the design has a concept, if possible a card people can use (to ensure they keep the card)
• ** I LIKE THIS CONCEPT: http://plovix.example/wp-content/uploads/2014/04/beautiful-creative-unique-original-impressive-business-cards-designs-18.jpg
• And the DESIGN I thought of has a silhouette of a woman sleeping on top of front of card and if you flip the card over there's a silhouette of a man sleeping on the bottom of the back of the card. IF you put 2 cards together (back to front) it looks like they are sleeping together.
• INSIDE pull out card can be designed later.
• See our website and videos for images we've used in the past.
• We are open to new concepts, images, stories.
• Must be story / people driven. Mattress sales are driven by the idea of good sleep, solving sleep issues and making people happy.
Nice to have
• Just some examples.... adding a feature to the card like a Sleep positions chart or NFC chip or something interesting. I am open to ideas and printing on unique materials... like soft vinyl fabric.
Should not have
• not dull in colour or concept

```html
<!DOCTYPE html>
<html lang="en">
<head>
<meta charset="utf-8">
<title>Trellis Rest business card</title>
<link rel="stylesheet" href="https://fonts.googleapis.com/css2?family=Arimo:wght@400;700&family=Questrial&display=swap">
<style>
  :root {
    --backdrop: #d9d9d9;
    --card: #ffffff;
    --ink: #111111;
    --navy: #2d3590;
    --brand-grey: #3a3a3a;
    --sky: #1e9ad6;
    --sky-light: #8fd3f2;
    --harbor: #1c63ad;
    --harbor-text: #1f6fbd;
  }
  * { margin: 0; padding: 0; box-sizing: border-box; }
  html, body { width: 992px; height: 1200px; overflow: hidden; }
  body { background: var(--backdrop); position: relative; font-family: "Arimo", Arial, sans-serif; color: var(--ink); }

  .card { position: absolute; left: 98px; width: 808px; height: 462px; background: var(--card); overflow: hidden; }
  .card--front { top: 103px; }
  .card--back { top: 623px; }

  .band { position: absolute; left: 0; width: 100%; background: var(--sky); }
  .card--front .band { top: 429px; height: 33px; }
  .card--back .band { top: 435px; height: 27px; }

  .accent { position: absolute; }
  .card--front .accent { left: 0; top: 390px; }
  .card--back .accent { right: 0; top: 397px; }

  .brand { position: absolute; left: 48px; top: 236px; display: flex; align-items: center; gap: 14px; }
  .brand__mark { width: 26px; height: 26px; background: var(--sky); }
  .brand__name { font-family: "Questrial", Arial, sans-serif; font-size: 42px; color: var(--brand-grey); white-space: nowrap; }

  .person { position: absolute; right: 26px; top: 148px; text-align: right; }
  .person__name { font-family: "Questrial", Arial, sans-serif; font-size: 39px; line-height: 42px; color: var(--navy); }
  .person__title { font-size: 23px; line-height: 28px; }

  .contacts { position: absolute; right: 28px; top: 262px; list-style: none; }
  .contacts li { display: flex; justify-content: flex-end; align-items: center; height: 32px; font-size: 21px; }
  .contacts svg { margin-left: 18px; width: 16px; height: 16px; }

  .harbor-web { position: absolute; left: 54px; top: 314px; font-size: 33px; color: var(--harbor-text); }
  .harbor-badge { position: absolute; left: 457px; top: 33px; width: 264px; height: 264px; border-radius: 50%; background: var(--harbor); }
  .harbor-name { position: absolute; left: 404px; top: 312px; width: 366px; text-align: center; font-weight: 700; font-size: 40px; letter-spacing: 6px; color: var(--harbor); white-space: nowrap; }
</style>
</head>
<body>

<section class="card card--front" aria-label="Card front">
  <div class="brand">
    <span class="brand__mark"></span>
    <span class="brand__name">Trellis Rest</span>
  </div>

  <div class="person">
    <p class="person__name">Miriam Okafor</p>
    <p class="person__title">CEO &amp; Sleep Enthusiast</p>
  </div>

  <ul class="contacts">
    <li>416.555.0193
      <svg viewBox="0 0 16 16"><rect width="16" height="16" fill="#2d3590"/><rect x="5" y="3" width="6" height="10" rx="1" fill="none" stroke="#fff" stroke-width="1.3"/></svg>
    </li>
    <li>www.trellisrest.example
      <svg viewBox="0 0 16 16"><rect width="16" height="16" fill="#2d3590"/><circle cx="8" cy="8" r="4.5" fill="none" stroke="#fff" stroke-width="1.3"/><path d="M3.5 8h9M8 3.5c-2 2.5-2 6.5 0 9M8 3.5c2 2.5 2 6.5 0 9" fill="none" stroke="#fff" stroke-width="1"/></svg>
    </li>
    <li>miriam@trellisrest.example
      <svg viewBox="0 0 16 16"><rect width="16" height="16" fill="#2d3590"/><rect x="3" y="5" width="10" height="7" fill="#fff"/><path d="M3 5l5 4 5-4" fill="none" stroke="#2d3590" stroke-width="1"/></svg>
    </li>
    <li>4829 Varley Crescent Mississauga ON L5R 2T6 Canada
      <svg viewBox="0 0 16 16"><rect width="16" height="16" fill="#2d3590"/><path d="M8 13s-3.5-4-3.5-6.3a3.5 3.5 0 0 1 7 0C11.5 9 8 13 8 13z" fill="#fff"/><circle cx="8" cy="6.7" r="1.3" fill="#2d3590"/></svg>
    </li>
  </ul>

  <svg class="accent" width="320" height="32" viewBox="0 0 320 32"><polygon points="0,0 240,0 320,32 0,32" fill="var(--sky-light)"/></svg>
  <div class="band"></div>
</section>

<section class="card card--back" aria-label="Card back">
  <div class="harbor-badge"></div>
  <p class="harbor-name">DOZE HARBOR</p>
  <p class="harbor-web">dozeharbor.example</p>

  <svg class="accent" width="322" height="32" viewBox="0 0 322 32"><polygon points="40,0 322,0 322,32 0,32" fill="var(--sky-light)"/></svg>
  <div class="band"></div>
</section>

</body>
</html>
```